Business card

We are looking for a creative person to deigns our company business card.

Target Market(s)

College age student

Industry/Entity Type

Accommodation

Contact Information for Business Card

We want a fun, clean and sophisticated design. It should look good, but more importantly the information should be legible.

Font styles to use
Serif
Sans Serif
Other font styles liked:
• Open Sans ,

Colors
33a6d7

Requirements
Must have
• Must have a young and memorable message. Be legible.
• Our logo on the back on a solid blue , please find color and logo attached
• LodgeBridgely.net on the back.
Nice to have
• I would like to have couple of different fonts on the LodgeBridgely.net on the back of the cards with a solid blue.

```html
<!DOCTYPE html>
<html lang="en">
<head>
<meta charset="utf-8">
<title>LodgeBridgely Business Card</title>
<link rel="stylesheet" href="https://fonts.googleapis.com/css2?family=EB+Garamond:wght@400&family=Open+Sans:wght@400;700&display=swap">
<style>
  :root {
    --bg: #e4e6e8;
    --card: #ffffff;
    --ring-light: #3399cc;
    --ring-dark: #175a8c;
    --brand-dark: #1d5f94;
    --ink: #111111;
  }
  * { margin: 0; padding: 0; box-sizing: border-box; }
  html, body { width: 1200px; height: 800px; overflow: hidden; background: var(--bg); }
  .canvas { position: relative; width: 1200px; height: 800px; }
  .card {
    position: absolute; left: 327px; width: 534px; height: 305px;
    background: var(--card); overflow: hidden;
  }
  .card--front { top: 34px; }
  .card--back { top: 434px; }
  .card__rings { position: absolute; inset: 0; width: 100%; height: 100%; }
  .serif { font-family: "EB Garamond", Georgia, serif; color: var(--ink); }
  .sans { font-family: "Open Sans", Arial, sans-serif; color: var(--ink); }
  .abs { position: absolute; white-space: nowrap; line-height: 1; }
  .centered { left: 0; right: 0; text-align: center; }

  .brand-name {
    top: 132px; font-family: "Open Sans", Arial, sans-serif; font-weight: 700;
    font-size: 34px; color: var(--brand-dark); letter-spacing: -0.5px;
  }

  .holder-name { top: 48px; font-size: 36px; left: 0; right: 0; text-align: center; padding-left: 10px; }
  .holder-role { top: 80px; font-size: 19px; left: 0; right: 0; text-align: center; padding-right: 16px; }
  .contact-text { font-size: 15px; }
  .address-line { font-size: 14.5px; left: 301px; }
  .icon { position: absolute; fill: var(--ink); }
  .web { top: 218px; font-size: 13.5px; }
  .find { top: 240px; font-size: 13.5px; }
  .handle { top: 258px; font-size: 13px; color: var(--brand-dark); }
</style>
</head>
<body>
<main class="canvas">

  <section class="card card--front">
    <svg class="card__rings" viewBox="0 0 534 305" aria-hidden="true">
      <ellipse cx="267" cy="152" rx="250" ry="151" fill="none" stroke="var(--ring-light)" stroke-width="10"/>
      <ellipse cx="267" cy="152" rx="226" ry="138" fill="none" stroke="var(--ring-dark)" stroke-width="3"/>
    </svg>
    <div class="abs centered brand-name">LodgeBridgely</div>
  </section>

  <section class="card card--back">
    <svg class="card__rings" viewBox="0 0 534 305" aria-hidden="true">
      <ellipse cx="267" cy="152" rx="250" ry="151" fill="none" stroke="var(--ring-light)" stroke-width="10"/>
      <ellipse cx="267" cy="152" rx="226" ry="138" fill="none" stroke="var(--ring-dark)" stroke-width="3"/>
    </svg>

    <div class="abs serif holder-name">Name here</div>
    <div class="abs serif holder-role">Founder</div>

    <svg class="icon" style="left:67px;top:127px" width="17" height="17" viewBox="0 0 24 24" aria-hidden="true">
      <path d="M6.6 10.8c1.4 2.8 3.8 5.1 6.6 6.6l2.2-2.2c.3-.3.7-.4 1-.2 1.1.4 2.3.6 3.6.6.6 0 1 .4 1 1V20c0 .6-.4 1-1 1C10.6 21 3 13.4 3 4c0-.6.4-1 1-1h3.5c.6 0 1 .4 1 1 0 1.3.2 2.5.6 3.6.1.3 0 .7-.2 1L6.6 10.8z"/>
    </svg>
    <div class="abs serif contact-text" style="left:102px;top:133px">206-555-0148</div>

    <svg class="icon" style="left:66px;top:158px" width="20" height="14" viewBox="0 0 20 14" aria-hidden="true">
      <path d="M0 0h20v14H0z M1.5 1.5v.4L10 8l8.5-6.1v-.4z M1.5 3.7v8.8h17V3.7L10 9.8z" fill-rule="evenodd"/>
    </svg>
    <div class="abs serif contact-text" style="left:102px;top:159px">maya@lodgebridgely.net</div>

    <svg class="icon" style="left:266px;top:128px" width="15" height="21" viewBox="0 0 15 21" aria-hidden="true">
      <path d="M7.5 0C3.4 0 0 3.3 0 7.4 0 12.8 7.5 21 7.5 21S15 12.8 15 7.4C15 3.3 11.6 0 7.5 0zm0 10.3a3 3 0 110-6 3 3 0 010 6z"/>
    </svg>
    <div class="abs serif address-line" style="top:131px;font-size:15px">Harborview North 10412</div>
    <div class="abs serif address-line" style="top:151px">linden ave n.greenwood</div>
    <div class="abs serif address-line" style="top:173px;font-size:15px">Harborview South 2240</div>
    <div class="abs serif address-line" style="top:192px">6th ave s, tacoma</div>

    <div class="abs sans centered web">www.website.com</div>
    <div class="abs serif centered find">Find Us on:</div>
    <div class="abs serif centered handle">@lodgebridgely</div>
  </section>

</main>
</body>
</html>
```